Accounting firm needs a brochure

Accounting firm seeks a professional design for a brochure/leaflet to complement their website and promote their services to the local community (but not restricted to as we currently have clients on a
national scale) and attract new clients. The target audience are taxpayers from individuals and professionals to SMEs (small to medium entities). The final design should communicate our assistance in tax matters, offering business & financial advice and development of a long term relationship with the customer/client.
We are looking for a slick, polished and proficient design based on the colours of the company logo and website (blue/black/white). Pictures and logo can be used from the website (www.kestorvane.co) but does not have to be limited to these. Additional relevant pictures welcome. The firm already has a slogan of ‘Building Trust into Growth’ but I would rather not like to have this as the main caption/slogan to attract new clients on the front page. An eyecatching new caption would need to be created that would attract new clients. Any ideas (see below)?
The brochure itself can either be a half-fold (4 sides) or tri-fold (6 sides) depending on the quality of the information displayed on the brochure
The basic information to be displayed is the company logo, website address, email address, other contact details, memberships to Institutes etc. It may be worth having a QR code at the back so that individuals can save our information on their mobile phones.
With regards to the body of the brochure, the main content should be derived from the website, eg home page (established 40 years etc) and ‘What we offer’. Other references can be made to the business and tax resources available on the website including calculators, helpsheets & forms, providing regular tax tips, the offer of a complete business guide to “How to make more Profit” upon signing up as a client etc, Listing testimonials and the type of clients we deal with (ie Retailers, property developers and letting, subcontractors etc), fixed fee quotation etc
The following URLs may provide some ideas and potential caption. However, these are just a guide as the brochure should be unique and customized in line with our website
http://www.pamphlora.co.uk/catalogue/designs/flyers/?keywords=accountants&page=1&per_page=54&order=rank_desc&tag[18]=on&tag[63]=on&colour=
http://www.pressgrideon.com/Templates/Flyer/Financial-Services/Accounting-Bookkeeping/Template-Design-Library.aspx
http://www.yourartfulnook.com/accounting-bookkeeping-templates.aspx
https://www.folioquay.net/gallery/13605181/Accounting-and-Bookkeeping-Services-Flyers
Artwork/brochure would be required to be delivered in the following format
Format - PDF or JPEG
Colour - CMYK
Bleed - 3mm(if design runs to edge)
Safe Zone - 3mm
Resolution - 300dpi
References to being better than other accountants should be avoided.
Winner may be offered further work in the form of designing a billboard poster in the future.

```html
<!DOCTYPE html>
<html lang="en">
<head>
<meta charset="utf-8">
<title>Kestorvane &amp; Co – Brochure Spread</title>
<link rel="stylesheet" href="https://fonts.googleapis.com/css2?family=Roboto+Slab:wght@400;700;800&display=swap">
<style>
  :root {
    --brand-blue: #2b4a7e;
    --brand-navy: #20386a;
    --body-ink: #3b3b3b;
    --paper: #ffffff;
    --backdrop: #e8e8e8;
    --photo-grey-dark: #4a4d52;
    --photo-grey-light: #d9dadc;
    --photo-cool: #a9c3dd;
    --photo-warm: #a7b98f;
  }
  * { box-sizing: border-box; margin: 0; padding: 0; }
  html, body { width: 1200px; height: 800px; overflow: hidden; }
  body {
    background: var(--backdrop);
    font-family: "Roboto Slab", Georgia, serif;
    color: var(--body-ink);
  }
  .spread {
    position: absolute; left: 40px; top: 30px;
    width: 1120px; height: 740px;
    display: flex;
    box-shadow: 0 6px 24px rgba(0,0,0,0.18);
  }
  .page {
    position: relative; width: 560px; height: 740px;
    background: var(--paper); overflow: hidden;
  }
  .page--left { background: linear-gradient(to left, #e4e4e4 0, var(--paper) 26px); }
  .page--right { background: linear-gradient(to right, #e4e4e4 0, var(--paper) 26px); }

  .photo { position: absolute; }
  .photo--finance {
    left: 0; top: 0; width: 280px; height: 280px;
    background: linear-gradient(135deg, var(--photo-grey-dark) 0%, #8c8f94 40%, var(--photo-grey-light) 100%);
  }
  .photo-band { position: absolute; background: var(--brand-navy); }
  .photo-band--finance { left: 0; top: 280px; width: 280px; height: 12px; }

  .column { position: absolute; font-size: 9.5px; line-height: 13px; text-align: justify; }
  .column p { margin-bottom: 7px; }
  .column strong { color: var(--brand-blue); }

  .intro-column { left: 30px; top: 312px; width: 240px; font-size: 10.5px; line-height: 15px; }
  .intro-column p { margin-bottom: 9px; }
  .services-column { left: 300px; top: 16px; width: 236px; }

  .top-rule { position: absolute; left: 300px; top: 0; width: 236px; height: 7px; background: var(--brand-blue); }

  .section-title {
    color: var(--brand-blue); font-weight: 700; font-size: 19px; line-height: 24px;
    margin: 4px 0 6px; text-align: left;
  }
  .consultation-note { font-weight: 700; color: var(--brand-blue); }

  .offer-list { list-style: none; margin-bottom: 8px; }
  .offer-list li { padding-left: 12px; position: relative; text-align: left; }
  .offer-list li::before { content: "+"; position: absolute; left: 0; color: var(--brand-blue); font-weight: 700; }

  .footer-band { position: absolute; left: 0; bottom: 0; width: 560px; height: 40px; background: var(--brand-navy); }

  /* right page */
  .benefits-column { left: 30px; top: 28px; width: 240px; }
  .photo--growth {
    left: 0; top: 300px; width: 270px; height: 170px;
    background: linear-gradient(160deg, var(--photo-cool) 0%, #b9c9b4 55%, var(--photo-warm) 100%);
  }
  .photo-band--growth { left: 0; top: 470px; width: 270px; height: 10px; }
  .benefits-column--lower { left: 30px; top: 496px; width: 240px; }
  .approach-column { left: 292px; top: 28px; width: 240px; }

  .guarantee-box {
    position: absolute; left: 270px; top: 300px; width: 290px; height: 120px;
    background: var(--brand-blue); color: var(--paper);
    padding: 18px 22px 0 22px;
    font-size: 11px; line-height: 15px; font-weight: 700;
  }
  .client-quote {
    position: absolute; left: 292px; top: 448px; width: 244px;
    color: #2a2a2a; font-weight: 800; font-size: 16px; line-height: 22px;
  }
  .client-quote p { margin-bottom: 14px; }
  .corner-bar { position: absolute; left: 292px; bottom: 14px; width: 110px; height: 9px; background: var(--brand-navy); }
</style>
</head>
<body>
<main class="spread">
  <section class="page page--left">
    <div class="photo photo--finance" role="img" aria-label="Photo of a calculator and pen resting on a printed financial spreadsheet"></div>
    <div class="photo-band photo-band--finance"></div>
    <div class="top-rule"></div>

    <div class="column intro-column">
      <p>We are well established with over 40 years of reputable experience in providing professional services throughout the London region and mainland.</p>
      <p>We provide a specialist service ensuring cost effective, high value solutions for all your financial requirements.</p>
      <p>We strive to provide a remarkable level of prompt, client focused and highly proficient service to suit all needs, business or personal.</p>
      <p>With an extensive portfolio of clients, we have the relevant knowledge and experience to provide effective and efficient services to all across a broad spectrum. For quality advice call us for all your accountancy.</p>
    </div>

    <div class="column services-column">
      <h2 class="section-title">The Company</h2>
      <p>Kestorvane &amp; Co is a friendly and independent firm of accountants based in South East London.</p>
      <p>For all your accounts, audit, taxation and other business needs, contact Kestorvane &amp; Co for success and control of your business today.</p>
      <p class="consultation-note">All initial consultations are free of charge.</p>

      <h2 class="section-title">What we Offer</h2>
      <ul class="offer-list">
        <li>Accounts</li>
        <li>Taxation</li>
        <li>Self-Assessment Tax Return</li>
        <li>Company Formations &amp; Secretarial Services</li>
        <li>Audit &amp; Assurance Services</li>
        <li>Business Plans &amp; Advice</li>
        <li>HMRC Enquiries &amp; Investigations</li>
        <li>Payroll/CIS/VAT &amp; Book-keeping</li>
      </ul>

      <h2 class="section-title">Our Promises</h2>
      <p><strong>Fixed Fees.</strong> Quoted in advance of the work and related to the value of work to be completed so that you know where you stand. That is unless you prefer to be charged on an hourly basis. Get a fixed fee quote.</p>
      <p><strong>Unlimited Free Phone Support.</strong> You can call as much as you need without charge. It can be about anything tax, business ideas, just someone to use as a sounding board or whatever you need. If you need help and we can provide it on the phone, it's FREE.</p>
      <p><strong>Unlimited Free Meetings.</strong> Whenever you wish to meet up, any meetings at our offices are always provided FREE of charge. You have the right to these</p>
    </div>

    <div class="footer-band"></div>
  </section>

  <section class="page page--right">
    <div class="column benefits-column">
      <p>whenever you feel the need. Just call us to schedule the meeting.</p>
      <p><strong>FREE Initial Tax Review.</strong> To identify all the tax planning opportunities you are not presently taking advantage of.</p>
      <p><strong>Work On Time, Every Time.</strong> As long as information is provided on time, accounts are guaranteed for completion within 30 days, phone calls and e-mails returned within 24 hours max but usually sooner.</p>
      <p><strong>Our Complete Guide To How To Make More Profit.</strong> Using proven business strategies which is probably worth at least £500 is provided FREE to all new clients.</p>
    </div>

    <div class="photo photo--growth" role="img" aria-label="Photo of cupped hands holding coins with a green seedling growing from them"></div>
    <div class="photo-band photo-band--growth"></div>

    <div class="column benefits-column--lower">
      <p><strong>FREE Tax Tips.</strong> Relevant to business owners delivered to you by E-mail through our regular E-Tax Tips &amp; News to help you pay less tax. Register here to receive Tax Tips &amp; News.</p>
      <p><strong>Someone to Sort All Your Paperwork.</strong> We understand doing the paperwork can be stressful for many business</p>
    </div>

    <div class="column approach-column">
      <p>owners who really just want to get on with running and building their business. So if you wish, we can take all the book-keeping, payroll and other paperwork off of you as well as the normal annual accounts and tax work.</p>
      <p><strong>A Flexible Accountant Who Speaks Plain English.</strong> There's no technical speak from us. We speak to you openly and honestly and promise not to blind you with jargon. We want you to feel comfortable to pick up the phone to us whenever you need for whatever you want and know you'll get good sound understandable advice. We will work with you in the way that suits you - in person, on the phone or online.</p>
    </div>

    <aside class="guarantee-box">
      Use our services to help you pay less tax and increase wealth, completely at our risk. Our services are so outstanding there's a 100% Risk Free Guarantee.
    </aside>

    <blockquote class="client-quote">
      <p>“We appreciate that only in time can we gain your trust, so that you know when we say we can and will do something, we do it.</p>
      <p>We hope to get that opportunity.”</p>
    </blockquote>

    <div class="corner-bar"></div>
  </section>
</main>
</body>
</html>
```